Business Card Design

The image I attached was a quick thought to my design. I have triplets and was invisioning something with three figures with maybe the colors blue, pink and green. I would like it to look very chic and modern yet soothing/healing. I will take any fresh ideas as well.

Side 1: Contact Details
Side 2: Appointment section (mandatory)

Thank u all for your preliminary designs. I had sent the old design over and am looking for a bold fresh NEW LOOK  for CORE MOTION. I saw some really creative ideas in the gallery. If you have any other questions please feel free to email me at rtbaxley@plumnet.example.

Thanks

Please keep in mind that it is mandatory that on the back of the card is for appointments.

Thank you.

Reason: The two mandatory elements that need to be on the card is that her title needs to read as so:

Reason: The criteria is still not being met. Her title needs to read as so: Dr. Marcia Whitfield, P.T., D.P.T. Doctor of Physical Therapy and The appointment info must go on the BACK of the card. Looking forward to some more great designs. Thanks.

Industry/Entity Type

Business

Contact Information for Business Card

Core Motion
Physical & Aquatic Therapy
Dr. Marcia Whitfield, P.T., D.P.T.
Doctor of Physical Therapy

22-37 B Birchmere Lane
Maple Hollow, N.Y. 10482
(Located inside of the Pulse gym in the KMR shopping center)

Phone & Fax: (555) 812-4076
Kbrask7@quillmail.example

Requirements
Must have
• One the back I would like to do an appointment layout.

```html
<!DOCTYPE html>
<html lang="en">
<head>
<meta charset="utf-8">
<title>Core Motion – Business Card</title>
<link href="https://fonts.googleapis.com/css2?family=Open+Sans:wght@300;400;600;700&display=swap" rel="stylesheet">
<style>
  :root {
    --green: #8dc63f;
    --blue: #a6dbe3;
    --pink: #d7286f;
    --ink: #4a4a4a;
    --grey: #8a8a8a;
    --rule: #d9d9d9;
    --paper: #ffffff;
    --bg: #e9e9e7;
    --photo-a: #e4edf5;
    --photo-b: #3f86c9;
  }
  * { box-sizing: border-box; margin: 0; padding: 0; }
  html, body {
    width: 1200px; height: 1000px; overflow: hidden;
    background: var(--bg);
    font-family: "Open Sans", Arial, sans-serif;
  }
  .sheet {
    width: 1200px; height: 1000px;
    display: flex; align-items: center; justify-content: center; gap: 60px;
  }
  .card {
    position: relative;
    width: 525px; height: 300px;
    background: var(--paper);
    box-shadow: 0 8px 24px rgba(0,0,0,.12);
    overflow: hidden;
  }

  /* Appointment side */
  .card-appointment .photo {
    position: absolute; left: 0; top: 0; width: 235px; height: 300px;
    background: radial-gradient(ellipse at 45% 55%, var(--photo-b) 0%, #9cc1e2 45%, var(--photo-a) 80%);
  }
  .card-appointment .brand-band {
    position: absolute; left: 245px; right: 0; top: 50px; height: 62px;
    background: var(--green); color: #fff; padding: 8px 0 0 16px;
  }
  .brand-name { font-weight: 700; font-size: 17px; letter-spacing: .5px; line-height: 1.2; }
  .brand-tag { font-weight: 400; font-size: 17px; line-height: 1.3; }
  .card-appointment .accent-strip {
    position: absolute; left: 245px; right: 18px; top: 112px; height: 6px; background: var(--blue);
  }
  .card-appointment .accent-square {
    position: absolute; right: 0; top: 112px; width: 18px; height: 12px; background: var(--pink);
  }
  .location {
    position: absolute; left: 262px; top: 134px; width: 250px;
    font-size: 12.5px; line-height: 1.45; color: var(--grey); font-weight: 400;
  }
  .location strong { color: var(--ink); font-weight: 700; }
  .appt-title {
    position: absolute; left: 262px; top: 184px;
    color: var(--green); font-weight: 700; font-size: 14px; letter-spacing: .3px;
  }
  .appt-field {
    position: absolute; left: 262px; width: 240px;
    display: flex; align-items: flex-end; gap: 6px;
    font-size: 13px; color: var(--ink);
  }
  .appt-field .line { flex: 1; border-bottom: 1px solid var(--rule); height: 16px; }
  .appt-date { top: 215px; }
  .appt-time { top: 245px; }

  /* Contact side */
  .card-contact .name-band {
    position: absolute; left: 120px; top: 0; width: 285px; height: 78px;
    background: var(--green); color: #fff; padding: 14px 0 0 18px;
  }
  .person-name { font-weight: 700; font-size: 16px; line-height: 1.3; }
  .person-title { font-weight: 300; font-size: 12.5px; }
  .card-contact .block-blue {
    position: absolute; left: 405px; top: 0; width: 80px; height: 78px; background: var(--blue);
  }
  .card-contact .block-pink {
    position: absolute; left: 485px; top: 0; width: 40px; height: 78px; background: var(--pink);
  }
  .practice {
    position: absolute; left: 28px; top: 108px;
  }
  .practice .brand-name { color: var(--ink); font-size: 15px; }
  .practice .brand-tag { color: var(--green); font-size: 15px; }
  .address {
    margin-top: 8px; font-size: 12.5px; line-height: 1.45; color: var(--grey); font-style: normal;
  }
  .contact-lines {
    position: absolute; left: 250px; top: 200px;
    font-size: 12.5px; line-height: 1.5; color: var(--ink);
  }
</style>
</head>
<body>
<main class="sheet">

  <section class="card card-appointment" aria-label="Appointment side">
    <div class="photo" role="img" aria-label="Photo of a therapist guiding a patient stretching with a band on an exercise ball"></div>
    <div class="brand-band">
      <div class="brand-name">CORE MOTION</div>
      <div class="brand-tag">Physical &amp; Aquatic Therapy</div>
    </div>
    <div class="accent-strip"></div>
    <div class="accent-square"></div>
    <p class="location">Located inside of the Pulse gym<br>in the <strong>KMR shopping center</strong></p>
    <h2 class="appt-title">APPOINTMENT DETAILS</h2>
    <div class="appt-field appt-date"><span>Date:</span><span class="line"></span></div>
    <div class="appt-field appt-time"><span>Time:</span><span class="line"></span></div>
  </section>

  <section class="card card-contact" aria-label="Contact side">
    <div class="name-band">
      <div class="person-name">Dr. Marcia Whitfield, P.T., D.P.T.</div>
      <div class="person-title">Doctor of Physical Therapy</div>
    </div>
    <div class="block-blue"></div>
    <div class="block-pink"></div>
    <div class="practice">
      <div class="brand-name">CORE MOTION</div>
      <div class="brand-tag">Physical &amp; Aquatic Therapy</div>
      <address class="address">22-37 B Birchmere Lane<br>Maple Hollow, N.Y. 10482</address>
    </div>
    <div class="contact-lines">
      <div>Phone &amp; Fax: (555) 812-4076</div>
      <div>Kbrask7@quillmail.example</div>
    </div>
  </section>

</main>
</body>
</html>
```